Visitenkarten-Design für eine Privatpraxis für Physiotherapie
Zielgruppe
Privatpraxis für Physiotherapie
Aufgabenstellung
----- siehe Ausschreibung ------

```html
<!DOCTYPE html>
<html lang="de">
<head>
<meta charset="utf-8">
<title>Visitenkarte – Jonas Albrecht, Privatpraxis für Physiotherapie</title>
<link rel="stylesheet" href="https://fonts.googleapis.com/css2?family=Raleway:wght@300;400;500;600;700&display=swap">
<style>
  :root {
    --stage: #ab4027;
    --paper: #f5ebcb;
    --paper-light: #f9f2de;
    --gold: #d9b02a;
    --ink-grey: #6b6a66;
    --link-red: #d8402a;
    --rule-blue: #6f8a96;
  }
  html, body {
    margin: 0;
    padding: 0;
    width: 1200px;
    height: 1200px;
    overflow: hidden;
    background: var(--stage);
    font-family: "Raleway", sans-serif;
  }
  .stage {
    position: relative;
    width: 1200px;
    height: 1200px;
  }
  .corner-rule {
    position: absolute;
    width: 75px;
    height: 1px;
    background: var(--rule-blue);
  }
  .corner-rule--top { left: 53px; top: 50px; }
  .corner-rule--bottom { left: 1072px; top: 1149px; }

  .card {
    position: absolute;
    top: 194px;
    width: 525px;
    height: 811px;
    background: var(--paper);
    box-shadow: 0 4px 14px rgba(60, 15, 5, 0.35);
    overflow: hidden;
  }
  .card--contact { left: 59px; }
  .card--appointment { left: 616px; }

  .brand-circle {
    position: absolute;
    left: 50%;
    width: 120px;
    height: 120px;
    margin-left: -72px;
    border: 12px solid var(--gold);
    border-radius: 50%;
  }
  .brand-name {
    position: absolute;
    left: 0;
    right: 0;
    text-align: center;
    color: var(--gold);
    font-weight: 700;
    font-size: 30px;
    letter-spacing: 0.5px;
  }
  .card--contact .brand-circle { top: 76px; }
  .card--contact .brand-name { top: 226px; }
  .card--appointment .brand-circle { top: 59px; }
  .card--appointment .brand-name { top: 210px; }

  .text-block {
    position: absolute;
    left: 0;
    right: 0;
    margin: 0;
    text-align: center;
    color: var(--ink-grey);
    font-size: 19px;
    font-weight: 400;
    line-height: 24px;
  }
  .contact-name {
    display: block;
    font-size: 28px;
    font-weight: 600;
    line-height: 34px;
  }
  .contact-address { top: 340px; }
  .contact-phone { top: 476px; }
  .contact-booking { top: 558px; }
  .contact-hours { top: 640px; }
  .contact-web {
    top: 755px;
    color: var(--link-red);
    font-weight: 700;
    font-size: 16px;
  }

  .appointment-title {
    position: absolute;
    top: 310px;
    left: 0;
    right: 0;
    margin: 0;
    text-align: center;
    color: var(--gold);
    font-size: 30px;
    font-weight: 500;
  }
  .appointment-table {
    position: absolute;
    top: 371px;
    left: 54px;
    display: flex;
    gap: 12px;
  }
  .appointment-column { width: 203px; }
  .appointment-head {
    height: 49px;
    line-height: 49px;
    background: var(--gold);
    border-radius: 3px 3px 0 0;
    color: #fff;
    text-align: center;
    font-size: 22px;
    font-weight: 500;
  }
  .appointment-slot {
    height: 41px;
    border-bottom: 3px solid var(--gold);
  }
  .appointment-slot--first {
    height: 43px;
    background: var(--paper-light);
  }
  .appointment-note {
    position: absolute;
    top: 694px;
    left: 0;
    right: 0;
    margin: 0;
    text-align: center;
    color: var(--gold);
    font-size: 19px;
    font-weight: 400;
    line-height: 24px;
  }
</style>
</head>
<body>
<main class="stage">
  <span class="corner-rule corner-rule--top"></span>
  <span class="corner-rule corner-rule--bottom"></span>

  <section class="card card--contact">
    <span class="brand-circle"></span>
    <div class="brand-name">JONAS ALBRECHT</div>

    <p class="text-block contact-address">
      <span class="contact-name">Jonas Albrecht</span>
      Privatpraxis für Physiotherapie<br>
      Lindenhofer Weg 7<br>
      32105 Bad Salzhain
    </p>
    <p class="text-block contact-phone">
      Telefonnummer:<br>
      0 52 11 34 56 780
    </p>
    <p class="text-block contact-booking">
      Terminvereinbarung<br>
      ausschließlich telefonisch!
    </p>
    <p class="text-block contact-hours">
      Öffnungszeiten: Mo, Di, Do<br>
      7:30 Uhr – 11:30 Uhr &nbsp;// 14:00 Uhr – 17:00 Uhr
    </p>
    <p class="text-block contact-web">www.physiotherapie-albrecht.de</p>
  </section>

  <section class="card card--appointment">
    <span class="brand-circle"></span>
    <div class="brand-name">JONAS ALBRECHT</div>

    <h2 class="appointment-title">Ihr nächster Termin</h2>

    <div class="appointment-table">
      <div class="appointment-column">
        <div class="appointment-head">Datum</div>
        <div class="appointment-slot appointment-slot--first"></div>
        <div class="appointment-slot"></div>
        <div class="appointment-slot"></div>
        <div class="appointment-slot"></div>
        <div class="appointment-slot"></div>
      </div>
      <div class="appointment-column">
        <div class="appointment-head">Uhrzeit</div>
        <div class="appointment-slot appointment-slot--first"></div>
        <div class="appointment-slot"></div>
        <div class="appointment-slot"></div>
        <div class="appointment-slot"></div>
        <div class="appointment-slot"></div>
      </div>
    </div>

    <p class="appointment-note">
      Bitte denken Sie an die<br>
      rechtzeitige Absage von<br>
      Terminen 24h vorher!
    </p>
  </section>
</main>
</body>
</html>
```